Looking for a cool & simple business-card-design for digital agency

Hi!

We are a web agency that offers Reputation Management, Zorvik & Seo Services and software development. We like cool things, we like innovative styles.

We have uploaded our logo.

Project Deadline Extended Reason: Client does not want any designs with the colorful logo. Please send us submissions ONLY with the blac and white logo. What the client would like to see:1) Back of the card: is a silver logo on a black background2) front of the card with all the data, please use white background and black logo thank you Added Friday, May 8, 2015

Software

```html
<!DOCTYPE html>
<html lang="en">
<head>
<meta charset="utf-8">
<title>Velmora AG – Business Card</title>
<link href="https://fonts.googleapis.com/css2?family=Open+Sans:wght@400;600;700&display=swap" rel="stylesheet">
<style>
  :root {
    --page-bg: #d6d6d6;
    --card-white: #f7f7f5;
    --card-black: #1c1c1c;
    --ink: #1a1a1a;
    --ink-soft: #333333;
    --silver: #c4c4c4;
    --silver-soft: #e0e0e0;
  }
  * { margin: 0; padding: 0; box-sizing: border-box; }
  html, body {
    width: 1200px; height: 1200px; overflow: hidden;
    background: var(--page-bg);
    font-family: "Open Sans", Arial, sans-serif;
  }
  .sheet {
    width: 1200px; height: 1200px;
    display: flex; flex-direction: column; align-items: center; justify-content: center;
    gap: 50px;
  }
  .card {
    width: 840px; height: 480px; position: relative;
    box-shadow: 0 10px 30px rgba(0,0,0,0.18);
  }
  .card-front { background: var(--card-white); color: var(--ink); }
  .card-back { background: var(--card-black); color: var(--silver); }

  .brand { display: flex; align-items: center; gap: 16px; font-weight: 700; letter-spacing: 1px; }
  .brand-mark { display: block; }
  .card-front .brand { position: absolute; top: 44px; left: 180px; font-size: 46px; color: var(--ink); }
  .card-front .brand-mark { width: 36px; height: 36px; background: var(--ink); }
  .card-back .brand { position: absolute; top: 170px; left: 150px; font-size: 68px; color: var(--silver); }
  .card-back .brand-mark { width: 52px; height: 52px; background: var(--silver); }

  .person { position: absolute; top: 196px; left: 60px; }
  .person-name { font-weight: 700; font-size: 24px; letter-spacing: 0.3px; }
  .person-title { font-size: 20px; color: var(--ink-soft); margin-top: 2px; }

  .contact { position: absolute; top: 196px; right: 40px; list-style: none; text-align: right; font-size: 20px; line-height: 28px; color: var(--ink); }
  .contact li { display: flex; justify-content: flex-end; align-items: center; gap: 8px; }
  .contact .gap { margin-top: 22px; }
  .contact svg { width: 18px; height: 18px; flex: none; }
  .contact .no-icon { padding-right: 26px; }

  .domain { position: absolute; bottom: 60px; left: 230px; font-size: 24px; color: var(--silver-soft); }
</style>
</head>
<body>
<main class="sheet">
  <section class="card card-front" aria-label="Card front">
    <div class="brand"><span class="brand-mark"></span>Velmora AG</div>
    <div class="person">
      <p class="person-name">YOUR FULL NAME</p>
      <p class="person-title">Your title</p>
    </div>
    <ul class="contact">
      <li class="no-icon">Your company address line 1</li>
      <li>City zipcode line 2
        <svg viewBox="0 0 20 20"><circle cx="10" cy="10" r="10" fill="#1a1a1a"/><path d="M5 10.5 10 6l5 4.5M7 10v4h6v-4" fill="none" stroke="#fff" stroke-width="1.6"/></svg>
      </li>
      <li class="gap no-icon">012-345-6789</li>
      <li>012-345-6789
        <svg viewBox="0 0 20 20"><circle cx="10" cy="10" r="10" fill="#1a1a1a"/><path d="M7 5h2l1 3-1.3 1a6 6 0 0 0 2.3 2.3l1-1.3 3 1v2a1.5 1.5 0 0 1-1.5 1.5A8 8 0 0 1 5.5 6.5 1.5 1.5 0 0 1 7 5z" fill="#fff"/></svg>
      </li>
      <li>your email adress
        <svg viewBox="0 0 20 20"><circle cx="10" cy="10" r="10" fill="#1a1a1a"/><rect x="5" y="6.5" width="10" height="7" fill="none" stroke="#fff" stroke-width="1.4"/><path d="M5 7l5 4 5-4" fill="none" stroke="#fff" stroke-width="1.4"/></svg>
      </li>
      <li>www.yourdomain.com
        <svg viewBox="0 0 20 20"><circle cx="10" cy="10" r="10" fill="#1a1a1a"/><circle cx="10" cy="10" r="5.5" fill="none" stroke="#fff" stroke-width="1.2"/><ellipse cx="10" cy="10" rx="2.3" ry="5.5" fill="none" stroke="#fff" stroke-width="1.2"/><path d="M4.5 10h11" stroke="#fff" stroke-width="1.2"/></svg>
      </li>
    </ul>
  </section>

  <section class="card card-back" aria-label="Card back">
    <div class="brand"><span class="brand-mark"></span>Velmora AG</div>
    <p class="domain">www.yourdomain.com</p>
  </section>
</main>
</body>
</html>
```